Drone company needs a brochure design

We would like a brochure design which compliments our existing logo, website and business card designs.

www.bramblecrest.com.au

```html
<!DOCTYPE html>
<html lang="en">
<head>
<meta charset="utf-8">
<title>Bramblecrest – Brochure</title>
<link href="https://fonts.googleapis.com/css2?family=Exo+2:wght@500;600;700&display=swap" rel="stylesheet">
<style>
  :root {
    --sky: #4dd5fb;
    --ink: #17181c;
    --slate: #25353f;
    --paper: #ffffff;
    --fold: rgba(255,255,255,0.12);
  }
  html, body { margin: 0; padding: 0; overflow: hidden; background: var(--paper); }
  .brochure {
    position: relative;
    width: 1200px;
    height: 849px;
    overflow: hidden;
    background: var(--paper);
    font-family: "Exo 2", sans-serif;
  }
  .shapes { position: absolute; inset: 0; }
  .brand-name {
    position: absolute;
    margin: 0;
    font-weight: 700;
    letter-spacing: 0.5px;
  }
  .brand-name--cover { left: 40px; top: 148px; font-size: 46px; color: var(--ink); }
  .brand-name--flap { left: 600px; top: 204px; transform: translateX(-50%); font-size: 21px; color: var(--paper); }
  .brand-mark {
    display: inline-block;
    width: 14px; height: 14px;
    border-radius: 50%;
    background: var(--sky);
    margin-right: 12px;
    vertical-align: middle;
  }
  .headline {
    position: absolute;
    left: 838px; top: 26px;
    margin: 0;
    font-size: 33px;
    line-height: 34px;
    font-weight: 700;
    color: var(--sky);
    text-transform: uppercase;
  }
  .subline {
    position: absolute;
    left: 838px; top: 137px;
    margin: 0;
    font-size: 17px;
    line-height: 26px;
    font-weight: 700;
    color: var(--ink);
    text-transform: uppercase;
  }
  .service-title {
    position: absolute;
    right: 833px; top: 488px;
    margin: 0;
    text-align: right;
    font-size: 28px;
    line-height: 34px;
    font-weight: 600;
    color: var(--paper);
    text-transform: uppercase;
  }
  .website {
    position: absolute;
    right: 833px; top: 614px;
    margin: 0;
    font-size: 14px;
    font-weight: 500;
    color: var(--sky);
    text-transform: uppercase;
  }
  .contact {
    position: absolute;
    left: 400px; width: 400px; top: 666px;
    text-align: center;
    color: var(--sky);
    font-size: 13.5px;
    line-height: 20px;
    font-weight: 500;
    text-transform: uppercase;
  }
  .contact-icons { display: flex; justify-content: center; gap: 6px; margin-bottom: 10px; }
  .contact p { margin: 0; }
</style>
</head>
<body>
<div class="brochure">
  <svg class="shapes" width="1200" height="849" viewBox="0 0 1200 849" aria-hidden="true">
    <rect class="cover-dark" x="0" y="353" width="400" height="496" fill="var(--ink)"/>
    <rect class="base-band" x="0" y="600" width="1200" height="249" fill="var(--ink)"/>
    <polygon class="peak" points="0,600 599,0 799,200 799,600" fill="var(--sky)"/>
    <polygon class="corner" points="0,600 247,849 0,849" fill="var(--sky)"/>
    <polygon class="diamond-top" points="799,600 999,400 1199,600" fill="var(--sky)"/>
    <polygon class="diamond-bottom" points="799,600 1199,600 999,800" fill="var(--slate)"/>
    <line class="fold" x1="400" y1="200" x2="400" y2="849" stroke="var(--fold)" stroke-width="1"/>
    <line class="fold" x1="799.5" y1="600" x2="799.5" y2="849" stroke="var(--fold)" stroke-width="1"/>
  </svg>

  <p class="brand-name brand-name--cover"><span class="brand-mark"></span>Bramblecrest</p>
  <p class="brand-name brand-name--flap">Bramblecrest</p>

  <h1 class="headline">Let us<br>capture<br>your vision</h1>
  <p class="subline">And provide you with that<br>ultimate vantage!</p>

  <h2 class="service-title">Aerial<br>media<br>solution</h2>
  <p class="website">http://www.bramblecrest.com.au</p>

  <div class="contact">
    <div class="contact-icons">
      <svg width="18" height="18" viewBox="0 0 18 18" aria-label="Phone">
        <rect width="18" height="18" rx="2" fill="var(--sky)"/>
        <path d="M5.5 4 L7.5 4 L8.3 6.8 L7 7.8 Q8 10 10.2 11 L11.2 9.7 L14 10.5 L14 12.5 Q13.5 14 12 14 Q7.5 13.5 4.5 9.5 Q4 8 4 6 Q4 4.5 5.5 4 Z" fill="var(--ink)"/>
      </svg>
      <svg width="18" height="18" viewBox="0 0 18 18" aria-label="Email">
        <rect width="18" height="18" rx="2" fill="var(--sky)"/>
        <rect x="3.5" y="5" width="11" height="8" fill="none" stroke="var(--ink)" stroke-width="1.3"/>
        <path d="M3.5 5 L9 9.5 L14.5 5" fill="none" stroke="var(--ink)" stroke-width="1.3"/>
      </svg>
    </div>
    <p>040 555 0182</p>
    <p>contact@bramblecrest.com.au</p>
    <p>Albany, WA 6330</p>
  </div>
</div>
</body>
</html>
```